Health & Wellness Labels on two Vitamin type bottles.

Hello,

My company is Bright Meadow Vita and I'm looking to get (9) labels done for my health & wellness company as we caring all nature products. I would like all the labels showing an all nature look. I would like my company name at the top of the bottle. I would also like all nature colors such as green,light green and so on. All of the products are Capsules.

Here are all of the different products sizes:
8 Size bottles 200cc and label size 202.00mm X 95.00
1 Size bottle 120cc and label size 169.00mm X 76.00mm

Here are all of the different products:
Tidal Glow Weight Loss ( Size 200 )
Tidal Glow Hair Loss ( Size 200cc )
Tidal Glow Sleeping ( Size 200cc )
Tidal Glow Skin Care ( Size 200cc )
Tidal Glow Energy ( Size 200cc )
Tidal Glow Digestion ( Size 200cc )
Tidal Glow Cold ( Size 200cc )
Tidal Glow Pain ( Size 200CC )
Tidal Glow Cleansing ( Size 120cc )
The tidal glow cleansing is for cleaning out the body.

I have also uploaded my company logo.

```html
<!DOCTYPE html>
<html lang="en">
<head>
<meta charset="utf-8">
<title>Bright Meadow Vita – Tidal Glow Capsule Labels</title>
<link href="https://fonts.googleapis.com/css2?family=Lilita+One&family=Alegreya:ital,wght@1,700;1,800&family=Lora:ital,wght@0,400;1,400;1,600&display=swap" rel="stylesheet">
<style>
  :root {
    --page: #ffffff;
    --deep-green: #1f6e34;
    --mid-green: #39b54a;
    --leaf-green: #7cc242;
    --lime: #a8d65a;
    --pale: #f4fbe6;
    --white: #ffffff;
    --silver: #e4e8e6;
  }
  * { box-sizing: border-box; margin: 0; padding: 0; }
  html, body { width: 1200px; height: 1000px; overflow: hidden; background: var(--page); }
  .sheet { position: relative; width: 1200px; height: 1000px; }

  .label {
    position: absolute;
    width: 192px; height: 266px;
    overflow: hidden;
    background:
      radial-gradient(ellipse 70% 55% at 50% 52%, var(--white) 0%, var(--pale) 35%, var(--lime) 80%, var(--leaf-green) 100%);
  }
  .label--small { transform: scale(0.815); transform-origin: top left; }

  .brand-mark {
    position: absolute; left: 50%; top: 8px;
    width: 24px; height: 24px; margin-left: -12px;
    border-radius: 50%;
    background: var(--deep-green);
  }
  .brand-name {
    position: absolute; left: 0; right: 0; top: 50px;
    text-align: center;
    font-family: "Lora", serif; font-size: 15px; font-weight: 400;
    color: var(--deep-green);
  }
  .tagline {
    position: absolute; left: 8px; right: 8px; top: 80px;
    padding: 2px 0;
    text-align: center;
    font-family: "Lora", serif; font-style: italic; font-size: 9.5px;
    color: var(--deep-green);
    border-top: 1px solid var(--leaf-green);
    border-bottom: 1px solid var(--leaf-green);
  }
  .line-name {
    position: absolute; left: 0; right: 0; top: 112px;
    text-align: center;
    font-family: "Lilita One", sans-serif; font-size: 18px; letter-spacing: 0.5px;
    color: var(--deep-green);
    text-transform: uppercase;
  }
  .line-name sup { font-size: 6px; vertical-align: top; }
  .product-name {
    position: absolute; left: 0; right: 0; top: 134px;
    text-align: center;
    font-family: "Alegreya", serif; font-style: italic; font-weight: 800; font-size: 21px;
    color: var(--leaf-green);
  }
  .capsule-art {
    position: absolute; left: 76px; top: 160px;
    width: 48px; height: 64px;
    background: linear-gradient(180deg, var(--silver) 0%, var(--white) 100%);
  }
  .leaf-art {
    position: absolute; left: 4px; top: 198px;
    width: 46px; height: 42px;
    background: linear-gradient(180deg, var(--lime) 0%, var(--mid-green) 100%);
  }
  .capsule-note {
    position: absolute; left: 6px; top: 176px;
    font-family: "Alegreya", serif; font-style: italic; font-weight: 700; font-size: 7.5px; line-height: 1.15;
    color: var(--deep-green);
  }
  .volume {
    position: absolute; right: 12px; top: 226px;
    font-family: "Alegreya", serif; font-style: italic; font-weight: 700; font-size: 8px;
    color: var(--deep-green);
  }
  .band {
    position: absolute; left: 0; right: 0; bottom: 0; height: 27px;
    background: var(--mid-green);
    text-align: center;
    font-family: "Alegreya", serif; font-style: italic; font-weight: 800; font-size: 16px; line-height: 27px;
    color: var(--white);
  }
</style>
</head>
<body>
<main class="sheet">

  <article class="label" style="left:140px;top:41px">
    <span class="brand-mark"></span><p class="brand-name">Bright Meadow Vita</p>
    <p class="tagline">Health &amp; Wellness at it's best !!!</p>
    <p class="line-name">Tidal Glow<sup>™</sup></p><p class="product-name">Pain Relief</p>
    <div class="capsule-art" role="img" aria-label="Illustration: open capsule with herbs"></div>
    <div class="leaf-art" role="img" aria-label="Illustration: green leaf"></div>
    <p class="capsule-note">Vegetarian<br>Capsules</p><p class="volume">200cc</p>
    <p class="band">All Natural</p>
  </article>

  <article class="label" style="left:383px;top:41px">
    <span class="brand-mark"></span><p class="brand-name">Bright Meadow Vita</p>
    <p class="tagline">Health &amp; Wellness at it's best !!!</p>
    <p class="line-name">Tidal Glow<sup>™</sup></p><p class="product-name">Skin Care</p>
    <div class="capsule-art" role="img" aria-label="Illustration: open capsule with herbs"></div>
    <div class="leaf-art" role="img" aria-label="Illustration: green leaf"></div>
    <p class="capsule-note">Vegetarian<br>Capsules</p><p class="volume">200cc</p>
    <p class="band">All Natural</p>
  </article>

  <article class="label" style="left:627px;top:41px">
    <span class="brand-mark"></span><p class="brand-name">Bright Meadow Vita</p>
    <p class="tagline">Health &amp; Wellness at it's best !!!</p>
    <p class="line-name">Tidal Glow<sup>™</sup></p><p class="product-name">Energy</p>
    <div class="capsule-art" role="img" aria-label="Illustration: open capsule with herbs"></div>
    <div class="leaf-art" role="img" aria-label="Illustration: green leaf"></div>
    <p class="capsule-note">Vegetarian<br>Capsules</p><p class="volume">200cc</p>
    <p class="band">All Natural</p>
  </article>

  <article class="label" style="left:885px;top:41px">
    <span class="brand-mark"></span><p class="brand-name">Bright Meadow Vita</p>
    <p class="tagline">Health &amp; Wellness at it's best !!!</p>
    <p class="line-name">Tidal Glow<sup>™</sup></p><p class="product-name">Digestion</p>
    <div class="capsule-art" role="img" aria-label="Illustration: open capsule with herbs"></div>
    <div class="leaf-art" role="img" aria-label="Illustration: green leaf"></div>
    <p class="capsule-note">Vegetarian<br>Capsules</p><p class="volume">200cc</p>
    <p class="band">All Natural</p>
  </article>

  <article class="label" style="left:144px;top:365px">
    <span class="brand-mark"></span><p class="brand-name">Bright Meadow Vita</p>
    <p class="tagline">Health &amp; Wellness at it's best !!!</p>
    <p class="line-name">Tidal Glow<sup>™</sup></p><p class="product-name">Hair Loss</p>
    <div class="capsule-art" role="img" aria-label="Illustration: open capsule with herbs"></div>
    <div class="leaf-art" role="img" aria-label="Illustration: green leaf"></div>
    <p class="capsule-note">Vegetarian<br>Capsules</p><p class="volume">200cc</p>
    <p class="band">All Natural</p>
  </article>

  <article class="label" style="left:385px;top:370px">
    <span class="brand-mark"></span><p class="brand-name">Bright Meadow Vita</p>
    <p class="tagline">Health &amp; Wellness at it's best !!!</p>
    <p class="line-name">Tidal Glow<sup>™</sup></p><p class="product-name">Cold</p>
    <div class="capsule-art" role="img" aria-label="Illustration: open capsule with herbs"></div>
    <div class="leaf-art" role="img" aria-label="Illustration: green leaf"></div>
    <p class="capsule-note">Vegetarian<br>Capsules</p><p class="volume">200cc</p>
    <p class="band">All Natural</p>
  </article>

  <article class="label" style="left:619px;top:365px">
    <span class="brand-mark"></span><p class="brand-name">Bright Meadow Vita</p>
    <p class="tagline">Health &amp; Wellness at it's best !!!</p>
    <p class="line-name">Tidal Glow<sup>™</sup></p><p class="product-name">Sleeping</p>
    <div class="capsule-art" role="img" aria-label="Illustration: open capsule with herbs"></div>
    <div class="leaf-art" role="img" aria-label="Illustration: green leaf"></div>
    <p class="capsule-note">Vegetarian<br>Capsules</p><p class="volume">200cc</p>
    <p class="band">All Natural</p>
  </article>

  <article class="label" style="left:880px;top:365px">
    <span class="brand-mark"></span><p class="brand-name">Bright Meadow Vita</p>
    <p class="tagline">Health &amp; Wellness at it's best !!!</p>
    <p class="line-name">Tidal Glow<sup>™</sup></p><p class="product-name">Weight Loss</p>
    <div class="capsule-art" role="img" aria-label="Illustration: open capsule with herbs and measuring tape"></div>
    <div class="leaf-art" role="img" aria-label="Illustration: green leaf"></div>
    <p class="capsule-note">Vegetarian<br>Capsules</p><p class="volume">200cc</p>
    <p class="band">All Natural</p>
  </article>

  <article class="label label--small" style="left:520px;top:698px">
    <span class="brand-mark"></span><p class="brand-name">Bright Meadow Vita</p>
    <p class="tagline">Health &amp; Wellness at it's best !!!</p>
    <p class="line-name">Tidal Glow<sup>™</sup></p><p class="product-name">Cleansing</p>
    <div class="capsule-art" role="img" aria-label="Illustration: open capsule with herbs"></div>
    <div class="leaf-art" role="img" aria-label="Illustration: green leaf"></div>
    <p class="capsule-note">Vegetarian<br>Capsules</p><p class="volume">120cc</p>
    <p class="band">All Natural</p>
  </article>

</main>
</body>
</html>
```